lantern productions business cards design

design a clean look but creative business card for a production company, I'm a freelance producer and launching my startup, would like to keep a clean professional look but still creative

Target Market(s)

businesses

Industry/Entity Type

video production

Contact Information for Business Card

logo, name (Mark Ellis), Title (Producer), (MFA Filmmaking, CSPT Los Angeles), contact number & email ID

Colors

Designer to choose only greyscale colors for use in the design.

Requirements
Must have
• logo, black and white colors, you can play with their shades
Nice to have
• a unique design, not necessarily a typical size card
Should not have
• too colorful or playful

```html
<!DOCTYPE html>
<html lang="en">
<head>
<meta charset="utf-8">
<title>Lantern Productions – Business Cards</title>
<link rel="stylesheet" href="https://fonts.googleapis.com/css2?family=Outfit:wght@400;500;600;700&display=swap">
<style>
  :root {
    --ink: #111111;
    --card-dark: #1b1b1b;
    --paper: #ffffff;
    --backdrop-edge: #b4b4b4;
    --backdrop-mid: #e8e8e8;
  }
  * { box-sizing: border-box; margin: 0; padding: 0; }
  html, body {
    width: 1200px;
    height: 1200px;
    overflow: hidden;
  }
  body {
    background: linear-gradient(90deg, var(--backdrop-edge) 0%, var(--backdrop-mid) 50%, var(--backdrop-edge) 100%);
    font-family: "Outfit", sans-serif;
    color: var(--ink);
    position: relative;
  }
  .card {
    position: absolute;
    top: 340px;
    width: 520px;
    height: 520px;
  }
  .card--back {
    left: 50px;
    background: var(--card-dark);
    display: flex;
    align-items: center;
    justify-content: center;
  }
  .card--front {
    left: 630px;
    background: var(--paper);
  }

  .brand-mark {
    display: flex;
    align-items: center;
    gap: 14px;
    font-weight: 700;
    text-transform: uppercase;
  }
  .brand-mark__dot {
    border-radius: 50%;
    flex: none;
  }
  .card--back .brand-mark { color: var(--paper); font-size: 40px; letter-spacing: 0.5px; }
  .card--back .brand-mark__dot { width: 26px; height: 26px; background: var(--paper); }

  .frame {
    position: absolute;
    left: 62px;
    top: 64px;
    width: 398px;
    height: 395px;
    border: 1.5px solid var(--ink);
  }
  .line {
    position: absolute;
    left: 0;
    width: 100%;
    text-align: center;
    white-space: nowrap;
  }
  .line span {
    background: var(--paper);
    padding: 0 8px;
  }
  .company {
    top: 44px;
    font-weight: 700;
    font-size: 37px;
    line-height: 37px;
    letter-spacing: -0.5px;
    text-transform: uppercase;
  }
  .person-name { top: 158px; font-weight: 600; font-size: 25px; text-transform: uppercase; }
  .person-title { top: 186px; font-size: 16px; font-weight: 400; }
  .person-degree { top: 210px; font-size: 16px; font-weight: 400; letter-spacing: 0.6px; }

  .card--front .brand-mark {
    position: absolute;
    top: 296px;
    left: 50%;
    transform: translateX(-50%);
    font-size: 22px;
    gap: 8px;
  }
  .card--front .brand-mark__dot { width: 12px; height: 12px; background: var(--ink); }

  .contact { font-size: 15.5px; font-weight: 400; line-height: 18px; }
  .contact--street { top: 381px; }
  .contact--zip { top: 398px; }
  .contact--phone { top: 424px; }
  .contact--email { top: 448px; }
</style>
</head>
<body>
  <section class="card card--back" aria-label="Business card back">
    <div class="brand-mark"><span class="brand-mark__dot"></span>Lantern</div>
  </section>

  <section class="card card--front" aria-label="Business card front">
    <div class="frame"></div>
    <div class="line company"><span>Lantern</span><br>Productions</div>
    <div class="line person-name">Mark Ellis</div>
    <div class="line person-title">Producer</div>
    <div class="line person-degree">MFA Filmmaking, CSPT Los Angeles</div>
    <div class="brand-mark"><span class="brand-mark__dot"></span>Lantern</div>
    <div class="line contact contact--street">218 Orchard Row, Fairbury</div>
    <div class="line contact contact--zip">Zone 4, Veltria</div>
    <div class="line contact contact--phone">+0155 2048 7316</div>
    <div class="line contact contact--email"><span>mark@lanternprod.co</span></div>
  </section>
</body>
</html>
```